"Big Tula" Snow & Ice Melt Package Design

Our company, Korvin Seasonal Products manufactures ice melt for melting snow. We are in the process of developing a new bag design for an ice melt product called "Big Tula". It's a play on words obviously. The "Hot" is to reflect the power of the ice melt, :-). The bag dimentions are 14" x 26".
To get an idea of our current product packaging go to our website at http://www.korvinsp-example.com
Thank you and good luck.

Reason: Need more time for a few design updates. Thanks, Glen

Reason: Need one more day

```html
<!DOCTYPE html>
<html lang="en">
<head>
<meta charset="utf-8">
<title>Big Tula – Ice Melt Bag Front</title>
<link rel="stylesheet" href="https://fonts.googleapis.com/css2?family=Archivo+Black&display=swap">
<style>
  :root {
    --blue-deep: #13308a;
    --blue-mid: #1e4fb0;
    --blue-light: #2a66c9;
    --swoosh-red: #e43f22;
    --swoosh-shadow: rgba(0,0,0,0.55);
    --panel-black: #050505;
    --panel-dark: #1a1a1a;
    --title-yellow: #ffc23a;
    --title-orange: #ff8c1a;
    --title-red: #ee2a1c;
  }
  html, body {
    margin: 0;
    padding: 0;
    width: 1200px;
    height: 2230px;
    overflow: hidden;
    background: #ffffff;
  }
  .bag-front {
    position: relative;
    width: 1200px;
    height: 2230px;
    overflow: hidden;
    background: radial-gradient(ellipse at 50% 45%, var(--blue-light) 0%, var(--blue-mid) 45%, var(--blue-deep) 100%);
  }
  .swoosh-art {
    position: absolute;
    inset: 0;
    width: 1200px;
    height: 2230px;
  }
  .product-title {
    position: absolute;
    left: 0;
    width: 1200px;
    margin: 0;
    text-align: center;
    font-family: "Archivo Black", "Arial Black", sans-serif;
    font-weight: 400;
    line-height: 1;
    background: linear-gradient(180deg, var(--title-red) 0%, var(--title-orange) 28%, var(--title-yellow) 70%, var(--title-orange) 100%);
    -webkit-background-clip: text;
    background-clip: text;
    color: transparent;
    filter: drop-shadow(0 6px 4px rgba(0,0,0,0.6));
  }
  .product-title--top {
    top: 610px;
    font-size: 370px;
    letter-spacing: 10px;
  }
  .product-title--bottom {
    top: 1010px;
    font-size: 270px;
    letter-spacing: 14px;
  }
</style>
</head>
<body>
  <main class="bag-front">
    <svg class="swoosh-art" viewBox="0 0 538 1000" preserveAspectRatio="none" aria-hidden="false">
      <defs>
        <filter id="band-shadow" x="-10%" y="-10%" width="120%" height="130%">
          <feDropShadow dx="0" dy="6" stdDeviation="6" flood-color="#000" flood-opacity="0.55"/>
        </filter>
        <radialGradient id="fence-fill" cx="50%" cy="45%" r="60%">
          <stop offset="0%" stop-color="#222"/>
          <stop offset="100%" stop-color="#030303"/>
        </radialGradient>
      </defs>

      <!-- upper red swoosh -->
      <path class="swoosh-band swoosh-band--upper" filter="url(#band-shadow)"
            fill="var(--swoosh-red)"
            d="M0,275 C140,150 330,70 538,58 L538,205 C360,195 170,235 0,330 Z"/>

      <!-- lower red swoosh -->
      <path class="swoosh-band swoosh-band--lower" filter="url(#band-shadow)"
            fill="var(--swoosh-red)"
            d="M0,680 C150,745 330,760 538,575 L538,650 C420,780 240,860 60,885 C30,888 10,880 0,875 Z"/>

      <!-- central chain-link panel -->
      <path class="fence-panel" role="img" aria-label="Black panel with a white chain-link fence pattern"
            fill="url(#fence-fill)"
            d="M0,330 C170,235 360,195 538,205 L538,575 C330,760 150,745 0,680 Z"/>
    </svg>

    <h1 class="product-title product-title--top">BIG</h1>
    <p class="product-title product-title--bottom">TULA</p>
  </main>
</body>
</html>
```